Criação de Papelaria Profissional para Beleza
A empresa queria:
" Atendemos clientes adultos masculino, feminino, adolescentes para tratamentos estéticos diversos como acne, rejuvenescimento facial, redução de medidas faciais e corporais, depilação, tratamento de celulite, estrias, medicina capilar, laser, cicatrizes, manchas, melasma, pequenos vasos, poros dilatados, limpeza de pele "

```html
<!DOCTYPE html>
<html lang="pt-BR">
<head>
<meta charset="utf-8">
<title>Lumira Clínica Estética – Crachás</title>
<link rel="stylesheet" href="https://fonts.googleapis.com/css2?family=Montserrat:wght@400;500;600&display=swap">
<style>
  :root {
    --bg: #e8e9ea;
    --navy: #0f2340;
    --navy-deep: #0a1a31;
    --teal: #2aa59e;
    --teal-soft: #6fc7c1;
    --ink: #1d2b3f;
    --line: #55606e;
    --white: #ffffff;
    --paper-shade: #f1f3f5;
    --photo-a: #e9d8cc;
    --photo-b: #c9a98f;
  }
  * { box-sizing: border-box; margin: 0; padding: 0; }
  html, body { width: 1200px; height: 1200px; overflow: hidden; }
  body {
    background: var(--bg);
    font-family: "Montserrat", sans-serif;
    position: relative;
  }
  .badge {
    position: absolute;
    top: 215px;
    width: 456px;
    height: 770px;
    border-radius: 22px;
    overflow: hidden;
    box-shadow: 0 10px 30px rgba(0,0,0,.16);
  }
  .badge--front { left: 86px; background: linear-gradient(160deg, var(--navy) 0%, var(--navy-deep) 100%); }
  .badge--back { left: 658px; background: linear-gradient(180deg, var(--white) 0%, var(--white) 55%, var(--paper-shade) 100%); }
  .badge__band {
    position: absolute; left: 0; right: 0; bottom: 0; height: 24px;
    background: var(--teal);
  }
  .slot {
    position: absolute; top: 26px; left: 50%; transform: translateX(-50%);
    width: 96px; height: 16px; border-radius: 8px; background: var(--bg);
  }
  .brand {
    position: absolute; top: 135px; left: 0; right: 0;
    display: flex; align-items: center; justify-content: center; gap: 16px;
  }
  .brand__dot { width: 30px; height: 30px; border-radius: 50%; background: var(--teal); }
  .brand__name {
    font-weight: 500; font-size: 40px; line-height: 1.05; letter-spacing: 2px;
    text-transform: uppercase;
  }
  .brand__name small { display: block; font-size: 15px; letter-spacing: 4px; }
  .badge--front .brand__name { color: var(--white); }
  .badge--back .brand__name { color: var(--navy); }
  .photo {
    position: absolute; top: 288px; left: 114px; width: 228px; height: 292px;
    border-radius: 12px; border: 6px solid var(--white);
    background: linear-gradient(180deg, var(--photo-a) 0%, var(--photo-b) 100%);
  }
  .holder { position: absolute; top: 628px; left: 0; right: 0; text-align: center; }
  .holder__name { color: var(--teal-soft); font-size: 33px; font-weight: 500; }
  .holder__role { color: var(--white); font-size: 27px; font-weight: 400; margin-top: 4px; }

  .fields { position: absolute; top: 250px; left: 34px; right: 34px; }
  .field { margin-bottom: 14px; }
  .field__label { display: block; font-size: 18px; color: var(--ink); margin-bottom: 6px; }
  .field__box {
    height: 58px; border: 1.5px solid var(--line); border-radius: 8px;
    background: var(--white);
  }
  .rules {
    position: absolute; top: 566px; left: 34px; right: 34px;
    list-style: none; font-size: 18px; line-height: 1.4; color: var(--ink);
  }
  .contact {
    position: absolute; top: 688px; left: 34px; right: 34px;
    display: flex; align-items: center; gap: 14px; font-size: 15px; color: var(--ink);
  }
  .contact__item { display: flex; align-items: center; gap: 10px; }
  .contact__icon {
    width: 38px; height: 38px; border-radius: 8px; background: var(--teal);
    display: flex; align-items: center; justify-content: center; flex: none;
  }
  .contact__address { font-size: 13px; line-height: 1.35; }
</style>
</head>
<body>

<section class="badge badge--front">
  <div class="slot"></div>
  <div class="brand">
    <span class="brand__dot"></span>
    <span class="brand__name">Lumira<small>Clínica Estética</small></span>
  </div>
  <div class="photo" role="img" aria-label="Foto de identificação da profissional"></div>
  <div class="holder">
    <p class="holder__name">Dra. Helena Marques</p>
    <p class="holder__role">Esteticista</p>
  </div>
  <div class="badge__band"></div>
</section>

<section class="badge badge--back">
  <div class="slot"></div>
  <div class="brand">
    <span class="brand__dot"></span>
    <span class="brand__name">Lumira<small>Clínica Estética</small></span>
  </div>
  <div class="fields">
    <div class="field"><span class="field__label">Nome:</span><div class="field__box"></div></div>
    <div class="field"><span class="field__label">RG:</span><div class="field__box"></div></div>
    <div class="field"><span class="field__label">DEPARTAMENTO:</span><div class="field__box"></div></div>
  </div>
  <ul class="rules">
    <li>- Crachá de uso pessoal e intransferível;</li>
    <li>- Uso obrigatório;</li>
    <li>- Deve ser portado em local visível.</li>
  </ul>
  <div class="contact">
    <div class="contact__item">
      <span class="contact__icon">
        <svg width="22" height="22" viewBox="0 0 24 24" aria-hidden="true"><path d="M6.6 10.8a15.1 15.1 0 0 0 6.6 6.6l2.2-2.2a1 1 0 0 1 1-.25 11.4 11.4 0 0 0 3.6.57 1 1 0 0 1 1 1V20a1 1 0 0 1-1 1A17 17 0 0 1 3 4a1 1 0 0 1 1-1h3.5a1 1 0 0 1 1 1c0 1.25.2 2.450.57 3.6a1 1 0 0 1-.25 1z" fill="#fff"/></svg>
      </span>
      <span>(11) 90000-4127</span>
    </div>
    <div class="contact__item">
      <span class="contact__icon">
        <svg width="22" height="22" viewBox="0 0 24 24" aria-hidden="true"><path d="M12 2a7 7 0 0 0-7 7c0 5.2 7 13 7 13s7-7.8 7-13a7 7 0 0 0-7-7zm0 9.5A2.5 2.5 0 1 1 12 6.5a2.5 2.5 0 0 1 0 5z" fill="#fff"/></svg>
      </span>
      <span class="contact__address">Rua das Acácias 218,<br>Vila Aurora, São Paulo</span>
    </div>
  </div>
  <div class="badge__band"></div>
</section>

</body>
</html>
```